Quillby Systems Business Card

Create an appealing and elegant Business card for quillby systems. Include logo and use related colors from website, be creative. Include Business name, my name, tile, address, contacts, address, and social media contacts if possible. Logo PSD file is attached.

Bleed Area: 3.46" x 2.32"
Trim: 3.3" x 2.16"
Safe Area: 3.14" x 2.02"

Save files as vector-based PDF with outlined text and PNG.
No crop marks
CMYK color setting

Business Card Info:

Quillby Systems

Dorian Vellacott
Owner

418 Bramlow Rd Unit C
Marrowfield, VT 02771
t. 1.888.562.3907
e. dorian.v@quillbysys.example
w. www.quillbysys.example

facebook. www.facebook.com/QuillbySys
twitter. twitter.com/quillbysys
pinterest. www.pinterest.com/quillbysys/

Target Market(s)

Business Owners and Partners

Industry/Entity Type

Business

Requirements
Must have
• Logo and related colors from website

```html
<!DOCTYPE html>
<html lang="en">
<head>
<meta charset="utf-8">
<title>Quillby Systems Business Card</title>
<link rel="stylesheet" href="https://fonts.googleapis.com/css2?family=Open+Sans:wght@400;600;700&display=swap">
<style>
  :root {
    --page: #e9e7e4;
    --ink: #2b2b2b;
    --muted: #4a4a4a;
    --brand-blue: #4a78b8;
    --card-black: #161616;
    --card-white: #ffffff;
  }
  * { box-sizing: border-box; margin: 0; padding: 0; }
  html, body {
    width: 1200px; height: 716px; overflow: hidden;
    background: var(--page);
    font-family: "Open Sans", Arial, sans-serif;
  }
  .stage {
    position: relative; width: 1200px; height: 716px;
    display: flex; align-items: center; justify-content: center; gap: 40px;
  }
  .card {
    position: relative; width: 540px; height: 309px;
    box-shadow: 0 6px 18px rgba(0,0,0,0.18);
    overflow: hidden;
  }
  /* Back side */
  .card-back {
    background: var(--card-black);
    display: flex; flex-direction: column; align-items: center; justify-content: center;
  }
  .card-back .wordmark {
    font-size: 40px; font-weight: 700; color: var(--brand-blue); letter-spacing: 0.5px;
  }
  .card-back .website {
    margin-top: 34px; font-size: 15px; color: var(--brand-blue);
  }
  /* Front side */
  .card-front { background: var(--card-white); color: var(--ink); }
  .card-front .wordmark {
    position: absolute; left: 36px; top: 34px;
    font-size: 30px; font-weight: 700; color: var(--brand-blue); line-height: 1;
  }
  .person {
    position: absolute; left: 36px; top: 98px;
    display: flex; align-items: baseline; gap: 14px;
  }
  .person .name { font-size: 17px; font-weight: 700; letter-spacing: 0.3px; }
  .person .title { font-size: 15px; color: var(--muted); }
  .contact {
    position: absolute; left: 36px; top: 140px;
    font-size: 13.5px; line-height: 21px; color: var(--ink);
  }
  .contact .label { color: var(--brand-blue); display: inline-block; width: 16px; }
  .social {
    position: absolute; left: 340px; top: 190px;
    list-style: none; font-size: 14px; line-height: 24px; color: var(--ink);
  }
  .social li { display: flex; align-items: center; gap: 10px; }
  .social .dot {
    width: 15px; height: 15px; border-radius: 50%; background: var(--brand-blue);
  }
  .band {
    position: absolute; left: 0; right: 0; bottom: 0; height: 13px;
    background: var(--brand-blue);
  }
</style>
</head>
<body>
  <main class="stage">
    <section class="card card-back" aria-label="Card back">
      <div class="wordmark">Quillby Systems</div>
      <div class="website">www.quillbysys.example</div>
    </section>

    <section class="card card-front" aria-label="Card front">
      <div class="wordmark">Quillby Systems</div>
      <div class="person">
        <span class="name">DORIAN VELLACOTT</span>
        <span class="title">Owner</span>
      </div>
      <div class="contact">
        <div><span class="label">T</span>1.888.562.3907</div>
        <div><span class="label">E</span>dorian.v@quillbysys.example</div>
        <div>418 Bramlow Rd Unit C</div>
        <div>Marrowfield, VT 02771</div>
      </div>
      <ul class="social">
        <li><span class="dot"></span>/QuillbySys</li>
        <li><span class="dot"></span>/quillbysys</li>
        <li><span class="dot"></span>/quillbysys/</li>
      </ul>
      <div class="band"></div>
    </section>
  </main>
</body>
</html>
```